Persian tea box like "halbrook and pennes " gift tea tin

We ran a competition previously on sketch hive and picked a design as winner and gave the prize, this design is good but needs refinement by a more professional designer .The design is for a retail box designed for a gift tea called Velmora Leaf and Clove,
our web site is www.velmoraleafandclove.example.
We have included the template for the box in the uploads , see files uploaded THIS MUST BE USED .
Perhaps the most appropriate would be :
For the professional designer to take these design files, (see uploads) , the student designer mocked up and make them look more professional , ie balance the layout , correct font size , colours etc ., this would be the most appropriate or if you chose do a new design with similar theme , ie a box like the halbrook and penne tea gift tins, ,see https://eu.halbrookandpenne.example/amber-dusk-blend-250g-loose-leaf-caddy

Target Market(s)

tea Gift market

Industry/Entity Type

afforable luxuary gifting

Colors
00AB8E
00BBA5
67D7C9
C6EFE9
E9F9F6

Requirements
Must have
• similar to Halbrook and pennes gift tea tins , similar colours, fonts etc
Should not have
• its not for suppermarket , its for gift stores

```html
<!DOCTYPE html>
<html lang="en">
<head>
<meta charset="utf-8">
<title>Velmora Leaf and Clove — Gift Tea Carton</title>
<link rel="stylesheet" href="https://fonts.googleapis.com/css2?family=Cinzel:wght@500;700&family=Cormorant+Garamond:wght@500;600&display=swap">
<style>
  :root {
    --page: #ffffff;
    --box: #86d6c6;
    --box-deep: #67d7c9;
    --mist: #c6efe9;
    --pale: #e9f9f6;
    --teal: #00ab8e;
    --ink: #1f3550;
    --cream: #fbf7ec;
    --gold: #c9a14a;
    --cut: #e0457b;
    --fold: #7aa9a1;
  }
  * { margin: 0; padding: 0; box-sizing: border-box; }
  html, body { width: 720px; height: 1200px; overflow: hidden; background: var(--page); }
  .carton-sheet { display: block; width: 720px; height: 1200px; }

  .panel-fill { fill: var(--box); }
  .arch-frame { fill: var(--mist); }
  .illustration-area { fill: url(#illustrationTone); }
  .label-card { fill: var(--cream); stroke: var(--gold); stroke-width: 3; }
  .label-inner { fill: none; stroke: var(--gold); stroke-width: 0.8; }
  .brand-mark-disc { fill: var(--ink); }

  .brand-name { font-family: "Cinzel", serif; font-weight: 700; fill: var(--ink); }
  .brand-sub { font-family: "Cinzel", serif; font-weight: 500; fill: var(--ink); letter-spacing: 2px; }
  .label-title { font-family: "Cinzel", serif; font-weight: 700; fill: var(--ink); }
  .label-line { font-family: "Cormorant Garamond", serif; font-weight: 600; fill: var(--ink); letter-spacing: 0.6px; }
  .mark-text { font-family: "Cinzel", serif; font-weight: 700; fill: var(--cream); }
  .side-copy { font-family: "Cormorant Garamond", serif; font-weight: 500; fill: var(--ink); }

  .cut-line { fill: none; stroke: var(--cut); stroke-width: 1; }
  .fold-line { fill: none; stroke: var(--fold); stroke-width: 0.8; stroke-dasharray: 4 3; }
  .flap-fill { fill: var(--box); }
</style>
</head>
<body>
<svg class="carton-sheet" viewBox="0 0 720 1200" xmlns="http://www.w3.org/2000/svg" xmlns:xlink="http://www.w3.org/1999/xlink">
  <defs>
    <linearGradient id="illustrationTone" x1="0" y1="0" x2="0" y2="1">
      <stop offset="0" stop-color="#e6ece9"/>
      <stop offset="1" stop-color="#9fb3ae"/>
    </linearGradient>

    <!-- brand face: name and arched illustration -->
    <symbol id="brandFace" viewBox="0 0 190 300">
      <rect class="panel-fill" x="0" y="0" width="190" height="300"/>
      <text class="brand-name" x="95" y="44" text-anchor="middle" font-size="27">VELMORA</text>
      <text class="brand-sub" x="95" y="60" text-anchor="middle" font-size="8">LEAF &amp; CLOVE</text>
      <path class="arch-frame" d="M26 300 V128 Q26 98 60 90 Q84 84 95 70 Q106 84 130 90 Q164 98 164 128 V300 Z"/>
      <rect class="illustration-area" x="46" y="122" width="98" height="108" rx="4" role="img" aria-label="Monochrome illustration of three women in traditional dress"/>
    </symbol>

    <!-- label face: product card -->
    <symbol id="labelFace" viewBox="0 0 190 300">
      <rect class="panel-fill" x="0" y="0" width="190" height="300"/>
      <rect class="label-card" x="22" y="100" width="146" height="112"/>
      <rect class="label-inner" x="28" y="106" width="134" height="100"/>
      <text class="label-title" x="95" y="142" text-anchor="middle" font-size="22">VELMORA</text>
      <text class="label-title" x="95" y="158" text-anchor="middle" font-size="11">SUPREME</text>
      <text class="label-line" x="95" y="174" text-anchor="middle" font-size="7">EARL GREY BLUE FLOWER</text>
      <text class="label-line" x="95" y="184" text-anchor="middle" font-size="7">BERGAMOT FLAVOUR</text>
      <text class="label-line" x="95" y="198" text-anchor="middle" font-size="5.5">NET WT 250g – 8.8 OZ</text>
    </symbol>
  </defs>

  <!-- Front faces -->
  <g class="front-faces">
    <use href="#brandFace" x="90" y="70" width="250" height="395"/>
    <use href="#labelFace" x="380" y="70" width="250" height="395"/>
  </g>

  <!-- Carton net -->
  <g class="carton-net">
    <!-- top lid with tuck on label panel -->
    <path class="flap-fill" d="M372 740 V660 H562 V740 Z"/>
    <path class="flap-fill" d="M380 660 Q380 626 410 624 H524 Q554 626 554 660 Z"/>
    <path class="cut-line" d="M372 740 V660 H380 Q380 626 410 624 H524 Q554 626 554 660 H562 V740"/>
    <line class="fold-line" x1="372" y1="740" x2="562" y2="740"/>
    <line class="fold-line" x1="380" y1="660" x2="554" y2="660"/>
    <circle class="brand-mark-disc" cx="467" cy="700" r="26"/>
    <text class="mark-text" x="467" y="703" text-anchor="middle" font-size="8">VELMORA</text>

    <!-- top dust flaps -->
    <path class="flap-fill cut-line" d="M272 740 L282 702 H362 L372 740"/>
    <path class="flap-fill cut-line" d="M562 740 L572 702 H652 L662 740"/>

    <!-- body panels -->
    <rect class="flap-fill" x="58" y="752" width="24" height="276"/>
    <path class="cut-line" d="M82 740 L58 752 V1028 L82 1040"/>
    <use href="#brandFace" x="82" y="740" width="190" height="300"/>
    <rect class="panel-fill" x="272" y="740" width="100" height="300"/>
    <use href="#labelFace" x="372" y="740" width="190" height="300"/>
    <rect class="panel-fill" x="562" y="740" width="100" height="300"/>

    <!-- side panel copy -->
    <g class="side-panel-left">
      <text class="side-copy" x="322" y="880" text-anchor="middle" font-size="6.5">Ingredients: black tea, bergamot</text>
      <text class="side-copy" x="322" y="890" text-anchor="middle" font-size="6.5">oil, cornflower petals.</text>
      <text class="side-copy" x="322" y="906" text-anchor="middle" font-size="6.5">Steep 3–5 minutes in</text>
      <text class="side-copy" x="322" y="916" text-anchor="middle" font-size="6.5">freshly boiled water.</text>
    </g>
    <g class="side-panel-right">
      <text class="brand-sub" x="612" y="800" text-anchor="middle" font-size="6">VELMORA</text>
      <text class="side-copy" x="612" y="900" text-anchor="middle" font-size="5.5">www.velmoraleafandclove.example</text>
    </g>

    <!-- body outline and folds -->
    <path class="cut-line" d="M82 740 H272 M82 1040 H272 M662 740 V1040 M82 740 V1040"/>
    <line class="fold-line" x1="272" y1="740" x2="272" y2="1040"/>
    <line class="fold-line" x1="372" y1="740" x2="372" y2="1040"/>
    <line class="fold-line" x1="562" y1="740" x2="562" y2="1040"/>
    <line class="fold-line" x1="82" y1="752" x2="82" y2="1028"/>

    <!-- bottom flaps -->
    <path class="flap-fill cut-line" d="M82 1040 V1088 Q82 1100 94 1100 H260 Q272 1100 272 1088 V1040"/>
    <path class="flap-fill cut-line" d="M272 1040 L284 1080 H360 L372 1040"/>
    <path class="flap-fill cut-line" d="M372 1040 V1088 Q372 1100 384 1100 H550 Q562 1100 562 1088 V1040"/>
    <path class="flap-fill cut-line" d="M562 1040 L574 1080 H650 L662 1040"/>
    <line class="fold-line" x1="82" y1="1040" x2="662" y2="1040"/>
  </g>
</svg>
</body>
</html>
```